Events By Quellon

Weddings, Corporate, Special Events
Memorable Catering, Personalized Menus, Custom Layout & Designs
Professional Staff, Excellent Service
Our Mission is Turning YOUR Vision into a Reality

Dorrie Quellon, Principal Planner
ph. 202 555-0187 - fax 301-555-0142
Email - eventsbyquellon@mailhaven.net
Web - www.cateringbyquellon.net
cateringbyquellon@Instagram

Target Market(s)

All Brides, Corprate Business, Special Events

Industry/Entity Type

Hospitality

Contact Information for Business Card

clean but affective

Font styles to use
Serif
Sans Serif
Script

Colors

Designer to choose colors to be used in the design.

Requirements
Must have
• logo with tagline using colors that will enhance what
• some pictures of nice table scape, hors d'oevures, upscale foods......
Nice to have
• Event: Something that happens or is regarded as happening, an occurrence especially one of some importance.
Should not have
• Use Logo on both sides

```html
<!DOCTYPE html>
<html lang="en">
<head>
<meta charset="utf-8">
<title>Events By Quellon – Business Card</title>
<link href="https://fonts.googleapis.com/css2?family=Cinzel:wght@400&family=Libre+Baskerville:wght@400;700&display=swap" rel="stylesheet">
<style>
  :root {
    --backdrop: #dcddde;
    --card: #231f20;
    --teal: #12a6b0;
    --ring: #8a8a8c;
    --muted: #a7a7a7;
    --ink: #ffffff;
  }
  * { margin: 0; padding: 0; box-sizing: border-box; }
  html, body { width: 1091px; height: 1200px; overflow: hidden; }
  body {
    background: var(--backdrop);
    position: relative;
    font-family: "Libre Baskerville", Georgia, serif;
    color: var(--ink);
  }
  .card {
    position: absolute;
    width: 374px;
    height: 656px;
    background: var(--card);
    border-radius: 44px;
    text-align: center;
  }
  .card--front { left: 128px; top: 289px; }
  .card--back { left: 587px; top: 286px; }
  .emblem-ring {
    position: absolute;
    left: 50%;
    width: 100px;
    height: 100px;
    margin-left: -50px;
    border: 3px solid var(--ring);
    border-radius: 50%;
  }
  .card--front .emblem-ring { top: 60px; }
  .card--back .emblem-ring { top: 81px; }
  .brand-name {
    position: absolute;
    left: 0; right: 0;
    font-size: 26px;
    color: var(--teal);
    line-height: 1;
  }
  .card--front .brand-name { top: 190px; }
  .card--back .brand-name { top: 213px; }
  .brand-tagline {
    position: absolute;
    left: 0; right: 0;
    font-family: "Cinzel", "Times New Roman", serif;
    font-size: 11px;
    letter-spacing: 0.3px;
    color: var(--muted);
  }
  .card--front .brand-tagline { top: 226px; }
  .card--back .brand-tagline { top: 250px; }
  .mission {
    position: absolute;
    top: 298px; left: 0; right: 0;
    font-weight: 700;
    font-size: 14.5px;
    line-height: 18px;
    letter-spacing: 0.3px;
  }
  .icon-row {
    position: absolute;
    left: 50%;
    transform: translateX(-50%);
  }
  .card--front .icon-row { top: 366px; }
  .card--back .icon-row { top: 413px; }
  .services {
    position: absolute;
    top: 410px; left: 0; right: 0;
    list-style: none;
    font-size: 15px;
    line-height: 25.1px;
  }
  .planner-name {
    position: absolute;
    top: 334px; left: 0; right: 0;
    font-weight: 700;
    font-size: 26px;
    color: var(--teal);
    letter-spacing: 0.5px;
  }
  .planner-title {
    position: absolute;
    top: 366px; left: 0; right: 0;
    font-size: 15px;
  }
  .contacts {
    position: absolute;
    top: 452px; left: 0; right: 0;
    list-style: none;
    font-size: 14.5px;
    line-height: 26.4px;
  }
</style>
</head>
<body>

<section class="card card--front">
  <div class="emblem-ring"></div>
  <div class="brand-name">Events By Quellon</div>
  <div class="brand-tagline">Events Designed with You in Mind</div>
  <p class="mission">Our Mission is Turning<br>YOUR Vision into a Reality</p>
  <svg class="icon-row" width="240" height="22" viewBox="0 0 240 22" aria-hidden="true">
    <g fill="var(--teal)">
      <circle cx="11" cy="11" r="11"/><circle cx="42" cy="11" r="11"/><circle cx="73" cy="11" r="11"/><circle cx="104" cy="11" r="11"/>
      <circle cx="135" cy="11" r="11"/><circle cx="166" cy="11" r="11"/><circle cx="197" cy="11" r="11"/><circle cx="228" cy="11" r="11"/>
    </g>
    <g fill="none" stroke="#fff" stroke-width="1.6">
      <circle cx="8.5" cy="12.5" r="4"/><circle cx="13.5" cy="12.5" r="4"/>
      <rect x="67" y="6" width="12" height="11" rx="1"/><line x1="67" y1="9.5" x2="79" y2="9.5"/>
      <line x1="129" y1="7" x2="141" y2="7"/><line x1="129" y1="11" x2="141" y2="11"/><line x1="129" y1="15" x2="141" y2="15"/>
      <path d="M222 11.5l4 4 7-8" stroke-width="2.2"/>
    </g>
    <g fill="#fff">
      <circle cx="42" cy="8" r="3"/><path d="M36 17c0-4 3-6 6-6s6 2 6 6z"/>
      <path d="M97 14c0-4 3-7 7-7s7 3 7 7z"/><rect x="96" y="15" width="16" height="1.6"/>
      <circle cx="166" cy="11" r="6"/>
      <circle cx="192" cy="8.5" r="2.2"/><circle cx="197" cy="7.5" r="2.4"/><circle cx="202" cy="8.5" r="2.2"/>
      <path d="M189 16c0-3 2-5 8-5s8 2 8 5z"/>
    </g>
    <g fill="var(--teal)"><circle cx="163.5" cy="9" r="1.2"/><circle cx="168" cy="9" r="1.2"/><circle cx="165" cy="13.5" r="1.2"/></g>
  </svg>
  <ul class="services">
    <li>Weddings</li>
    <li>Corporate</li>
    <li>Special Events</li>
    <li>Memorable Catering</li>
    <li>Personalized Menus</li>
    <li>Custom Layout &amp; Designs</li>
    <li>Professional Staff</li>
    <li>Excellent Service</li>
  </ul>
</section>

<section class="card card--back">
  <div class="emblem-ring"></div>
  <div class="brand-name">Events By Quellon</div>
  <div class="brand-tagline">Events Designed with You in Mind</div>
  <div class="planner-name">Dorrie Quellon</div>
  <div class="planner-title">Principal Planner</div>
  <svg class="icon-row" width="146" height="22" viewBox="0 0 146 22" aria-hidden="true">
    <g fill="var(--teal)">
      <circle cx="11" cy="11" r="11"/><circle cx="42" cy="11" r="11"/><circle cx="73" cy="11" r="11"/><circle cx="104" cy="11" r="11"/><circle cx="135" cy="11" r="11"/>
    </g>
    <path fill="#fff" d="M7 6l2.5-.5 1.5 3-1.5 1.2c.8 1.7 1.8 2.7 3.5 3.5l1.2-1.5 3 1.5-.5 2.5c-5 .5-10-4.5-9.7-9.7z"/>
    <g fill="#fff">
      <rect x="38" y="5" width="8" height="4"/><rect x="35" y="9" width="14" height="6" rx="1"/><rect x="38" y="13" width="8" height="4"/>
      <rect x="66" y="7" width="14" height="9" rx="1"/>
      <circle cx="104" cy="11" r="6"/>
    </g>
    <path d="M66 7.5l7 5 7-5" fill="none" stroke="var(--teal)" stroke-width="1.3"/>
    <path d="M98 11h12M104 5c-3 3-3 9 0 12M104 5c3 3 3 9 0 12" fill="none" stroke="var(--teal)" stroke-width="1"/>
  </svg>
  <ul class="contacts">
    <li>202 555-0187</li>
    <li>301-555-0142</li>
    <li>eventsbyquellon@mailhaven.net</li>
    <li>www.cateringbyquellon.net</li>
    <li>@cateringbyquellon</li>
  </ul>
</section>

</body>
</html>
```